Custom Business Card Design

We are looking for a raised spot logo design to use with Hearthline.com. We will provide the logo files. Should be a front and back design. We want to implement the house into the back design using the same colors as the logo through out. Something VERY cool!

```html
<!DOCTYPE html>
<html lang="en">
<head>
<meta charset="utf-8">
<title>Hearthline business cards</title>
<link href="https://fonts.googleapis.com/css2?family=Open+Sans:wght@400;600;700&display=swap" rel="stylesheet">
<style>
  :root {
    --backdrop: #3a322e;
    --card: #141414;
    --silver: #a9a9a9;
    --silver-dim: #7d7d7d;
    --brand-blue: #3a86c8;
    --brand-red: #e2343f;
    --ink-light: #f2f2f2;
    --divider: #5a5a5a;
  }
  * { box-sizing: border-box; margin: 0; padding: 0; }
  html, body { width: 1200px; height: 864px; overflow: hidden; }
  body {
    background: var(--backdrop);
    font-family: "Open Sans", Arial, sans-serif;
    display: flex;
    align-items: center;
    justify-content: center;
    gap: 40px;
  }
  .card {
    width: 540px;
    height: 309px;
    background: var(--card);
    border-radius: 3px;
    box-shadow: 0 12px 30px rgba(0,0,0,.45);
    position: relative;
  }
  .wordmark {
    font-weight: 700;
    letter-spacing: 0.5px;
    line-height: 1;
    white-space: nowrap;
  }
  /* Front */
  .card--front {
    display: flex;
    flex-direction: column;
    align-items: center;
    justify-content: center;
    gap: 30px;
  }
  .card--front .wordmark { font-size: 50px; color: var(--silver); }
  .front__url {
    color: var(--silver-dim);
    font-size: 15px;
    letter-spacing: 3px;
  }
  /* Back */
  .card--back { display: flex; align-items: center; }
  .back__brand {
    width: 290px;
    display: flex;
    justify-content: center;
  }
  .card--back .wordmark { font-size: 36px; color: var(--brand-blue); }
  .back__divider {
    width: 1px;
    height: 160px;
    background: linear-gradient(to bottom, transparent, var(--divider) 20%, var(--divider) 80%, transparent);
  }
  .back__contact { padding-left: 22px; color: var(--ink-light); font-size: 14px; line-height: 1.35; }
  .contact__name { color: var(--brand-blue); font-weight: 700; font-size: 14px; }
  .contact__role { color: var(--brand-red); font-size: 14px; margin-bottom: 4px; }
  .contact__address { margin-bottom: 2px; }
  .contact__list { list-style: none; }
  .contact__list li { display: flex; align-items: center; gap: 8px; }
  .contact__list svg { width: 11px; height: 11px; fill: var(--brand-blue); flex: none; }
</style>
</head>
<body>
  <section class="card card--front" aria-label="Card front">
    <p class="wordmark">Hearthline</p>
    <p class="front__url">www.hearthline.com</p>
  </section>

  <section class="card card--back" aria-label="Card back">
    <div class="back__brand">
      <p class="wordmark">Hearthline</p>
    </div>
    <div class="back__divider"></div>
    <div class="back__contact">
      <p class="contact__name">DANA WHITFIELD</p>
      <p class="contact__role">CEO/FOUNDER</p>
      <p class="contact__address">214 Larkspur Court<br>Fairview, Oregon 97024</p>
      <ul class="contact__list">
        <li><svg viewBox="0 0 12 12" aria-hidden="true"><path d="M1 2h10v2H8L7 3H5L4 4H1zM2 5h8l1 6H1z"/></svg>503 555 0142</li>
        <li><svg viewBox="0 0 12 12" aria-hidden="true"><path d="M3 0h6v12H3zM4 1v8h4V1z"/></svg>503 555 0187</li>
        <li><svg viewBox="0 0 12 12" aria-hidden="true"><path d="M3 0h6v4H3zM1 4h10v6H1zM3 9h6v3H3z"/></svg>503 555 0193</li>
        <li><svg viewBox="0 0 12 12" aria-hidden="true"><path d="M0 2h12v8H0zM1 3l5 4 5-4z"/></svg>dana@hearthline.com</li>
        <li><svg viewBox="0 0 12 12" aria-hidden="true"><circle cx="6" cy="6" r="6"/></svg>www.hearthline.com</li>
      </ul>
    </div>
  </section>
</body>
</html>
```